Postcard design to acquire new clients for my Property Management Company

I'm looking for a postcard design that I can send to prospective clients detailing information about my company and services.
Postcard should be eye catching and contain information from www.brightkeeplm.com. I've provided a few screen shots for the most important information and my logo.
Target Market(s)
Real Estate
Industry/Entity Type
Real Estate
Font styles to use
Sans Serif
Requirements
Must have
- Must be eye catching!! this will be a direct mail piece - I'd like for the card to be read and not tossed in the trash immediately.
Design que from the logo.
A place to write / print the receipts name and address.
our physical address - 2287 Marden Lane, Lubbock, TX 79382.
Should not have
- the contact information on the business card is not accurate - please use info from website.

```html
<!DOCTYPE html>
<html lang="en">
<head>
<meta charset="utf-8">
<title>Brightkeep Property Management – Postcard</title>
<link rel="stylesheet" href="https://fonts.googleapis.com/css2?family=Montserrat:wght@300;400;600;700;800&display=swap">
<style>
  :root {
    --navy: #1d4d86;
    --panel-deep: #1f4f86;
    --panel-mid: #3a6796;
    --panel-light: #5b84ad;
    --white: #ffffff;
    --stamp: #a0a09f;
    --rule: #a6a6a6;
    --paper: #ffffff;
  }
  * { margin: 0; padding: 0; box-sizing: border-box; }
  html, body { width: 1200px; height: 851px; overflow: hidden; background: var(--paper); }
  body { font-family: "Montserrat", Arial, sans-serif; }

  .postcard { position: relative; width: 1200px; height: 851px; background: var(--paper); }

  .offer-panel {
    position: absolute; left: 20px; top: 20px; width: 696px; height: 808px;
    color: var(--white); overflow: hidden;
  }
  .offer-panel__backdrop {
    position: absolute; inset: 0;
    background:
      radial-gradient(ellipse at 75% 35%, var(--panel-light) 0%, transparent 55%),
      linear-gradient(180deg, var(--panel-deep) 0%, var(--panel-mid) 55%, var(--panel-deep) 100%);
  }
  .offer-panel__content { position: relative; padding: 48px 0 0 26px; }

  .headline {
    font-weight: 700; font-size: 40px; line-height: 56px; letter-spacing: 0.5px;
    text-transform: uppercase;
  }
  .subhead {
    margin-top: 18px; font-weight: 400; font-size: 36px; line-height: 46px; letter-spacing: 0.5px;
  }

  .plans { margin-top: 78px; }
  .plan { position: relative; height: 121px; }
  .plan__name { font-weight: 700; font-size: 30px; line-height: 36px; text-transform: uppercase; }
  .plan__note { font-weight: 400; font-size: 30px; line-height: 44px; letter-spacing: 0.5px; }
  .plan__rate {
    position: absolute; left: 462px; top: 6px;
    font-weight: 800; font-size: 70px; line-height: 80px; letter-spacing: -1px;
  }

  .stamp-box { position: absolute; left: 1053px; top: 20px; width: 126px; height: 164px; background: var(--stamp); }

  .address-lines { position: absolute; left: 757px; top: 267px; width: 422px; }
  .address-lines span { display: block; height: 2px; background: var(--rule); margin-bottom: 67px; }

  .brand {
    position: absolute; right: 20px; top: 618px; text-align: right;
    color: var(--navy); font-weight: 600; text-transform: uppercase;
  }
  .brand__name { font-size: 37px; line-height: 40px; letter-spacing: 6px; margin-right: -6px; }
  .brand__tag { font-size: 17px; line-height: 22px; letter-spacing: 3.2px; margin-right: -3px; }

  .office {
    position: absolute; right: 84px; top: 724px; text-align: right;
    color: var(--navy); font-weight: 400; font-size: 28px; line-height: 41px;
  }
  .office-pin { position: absolute; left: 1130px; top: 728px; width: 50px; height: 68px; }
</style>
</head>
<body>
<main class="postcard">
  <section class="offer-panel">
    <div class="offer-panel__backdrop" role="img" aria-label="Photo of a two-storey house with trees, tinted blue"></div>
    <div class="offer-panel__content">
      <h1 class="headline">Choose the right<br>property management<br>system</h1>
      <p class="subhead">Selecting the wrong<br>manager could be your<br>costliest mistake ever</p>
      <div class="plans">
        <div class="plan">
          <h2 class="plan__name">Lease Only</h2>
          <p class="plan__note">You Just Need Tenants</p>
          <p class="plan__rate">9%</p>
        </div>
        <div class="plan">
          <h2 class="plan__name">Full Service</h2>
          <p class="plan__note">Our Most Popular</p>
          <p class="plan__rate">10%</p>
        </div>
        <div class="plan">
          <h2 class="plan__name">Premium Service</h2>
          <p class="plan__note">Our Premier Service</p>
          <p class="plan__rate">12%</p>
        </div>
      </div>
    </div>
  </section>

  <div class="stamp-box" aria-hidden="true"></div>

  <div class="address-lines" aria-hidden="true">
    <span></span><span></span><span></span><span></span><span></span>
  </div>

  <div class="brand">
    <p class="brand__name">Brightkeep</p>
    <p class="brand__tag">Property Management</p>
  </div>

  <address class="office">2287 Marden Lane<br>Lubbock, TX 79382</address>
  <svg class="office-pin" viewBox="0 0 50 68" aria-hidden="true">
    <path d="M25 2C12 2 2 12 2 25c0 17 23 41 23 41s23-24 23-41C48 12 38 2 25 2z" fill="var(--navy)"/>
    <circle cx="25" cy="25" r="16" fill="#fff"/>
    <path d="M14 26l11-10 11 10h-3v9h-5v-6h-6v6h-5v-9z" fill="var(--navy)"/>
  </svg>
</main>
</body>
</html>
```